Berichtslayout für Unternehmensberatung mit Schwerpunkt Softwareentwicklung für den Public Sektor
Wir sind eine Unternehmensberatung, die sich auf Softwareentwicklung für den Public Sektor spezialisiert hat (www.tqm-beratung.de). Unsere Zielgruppe sind Verwaltungen im deutschsprachigen Raum. Wir bieten für diesen Markt verschiedene Softwareprodukte an. Aus unseren Softwareprodukten werden automatische Controllingberichte erzeugt.
Company
We are a consulting company, that is specialised in softwaredevelopment regarding the public sector (www.tqm-beratung.de). Our customers are administrations all over Germany, Austria and Swiss. We offer different products to the market. One of which produces a report you can find enclosed to this project.
Aufgabenstellung
Es soll ein Berichtslayout erstellt werden.
• Das Berichtslayout muss die Informationen des Berichtsentwurfs aufnehmen können, beispielsweise Tabellen etc. (Anlage 1)
• Der Bericht enthält viel Text und viele Zahlen, weshalb auch ein Vorschlag über die Gestaltung der Tabellen enthalten sein soll. (Anlage 1)
• Das Layout kann Symbole wie den Falkmoorer Zeichen oder die Farben des Deckblatts aufnehmen (Anlage 2). Alle anderen Elemente können verändert werden.
• Schriftart muss Calibri sein.
• Das Berichtslayout soll übersichtlich und ansprechend aussehen.
• Das Berichtslayout soll, soweit möglich, nicht überladen wirken.
Der Bericht wird über jasper Reports erzeugt.
Wenn das Design in AI oder Indesign entwickelt wird, sollten wir dies verwenden können.
Task:
We need a better Layout for our report.
• The Layout has to be able to handle the informations shown in 'Anlage 1'.
• The layout can use Symbols like the 'Falkmoorer Zeichen' (Falkmoorer Sign) or colors of the covering page shown in 'Anlage 2'.
• Since the Layout has to handle a lot of numbers an text it would be nice if you could deliver a layout suggestion for those elements as well
• The Font has to be Calibri
• The Layout sould look as clean and appealing as possible.

```html
<!DOCTYPE html>
<html lang="de">
<head>
<meta charset="utf-8">
<title>Controlling Bericht – Inhalt</title>
<link href="https://fonts.googleapis.com/css2?family=Carlito:wght@400;700&display=swap" rel="stylesheet">
<style>
  :root {
    --bg: #efefef;
    --paper: #ffffff;
    --paper-shade: #f3f3f3;
    --red: #d42a2e;
    --red-light: #e0494c;
    --ink: #2b2b2b;
    --ink-soft: #555555;
    --photo-a: #c9c7c6;
    --photo-b: #8d7a70;
    --photo-c: #3f3f44;
  }
  * { box-sizing: border-box; margin: 0; padding: 0; }
  html, body { width: 1200px; height: 840px; overflow: hidden; }
  body {
    background: var(--bg);
    font-family: 'Carlito', 'Calibri', sans-serif;
    color: var(--ink);
  }
  .spread {
    position: absolute;
    left: 180px; top: 123px;
    width: 840px; height: 594px;
    display: flex;
    box-shadow: 0 12px 40px rgba(0,0,0,0.12);
  }
  .page {
    position: relative;
    width: 420px; height: 594px;
    background: var(--paper);
    overflow: hidden;
  }
  .page--left { background: linear-gradient(90deg, var(--paper) 85%, var(--paper-shade)); }
  .page--right { background: linear-gradient(90deg, var(--paper-shade), var(--paper) 15%); }

  .contents-art { position: absolute; inset: 0; }
  .contents-title {
    fill: #ffffff;
    font-family: 'Carlito', 'Calibri', sans-serif;
    font-weight: 700;
    font-size: 21px;
    letter-spacing: 3px;
  }
  .toc {
    position: absolute;
    left: 190px; top: 320px;
    list-style: none;
  }
  .toc__item { display: flex; align-items: flex-start; margin-bottom: 14px; }
  .toc__page {
    width: 46px;
    color: var(--red);
    font-size: 26px;
    line-height: 1;
    letter-spacing: 1px;
  }
  .toc__label { font-weight: 700; font-size: 13px; line-height: 1.1; }
  .toc__sub { font-size: 10px; color: var(--ink-soft); }

  .report-card {
    position: absolute;
    left: 62px; top: 120px;
    width: 316px; height: 420px;
    background: linear-gradient(160deg, var(--red-light), var(--red) 60%);
    color: #fff;
    padding: 62px 30px 0;
  }
  .report-card__title {
    text-align: center;
    font-weight: 700;
    font-size: 24px;
    line-height: 1.15;
    margin-bottom: 34px;
  }
  .report-card__row {
    display: grid;
    grid-template-columns: 130px 1fr;
    font-size: 13px;
    line-height: 1.2;
    margin-bottom: 16px;
  }
  .report-card__value { font-weight: 700; }
  .mark { display: inline-block; width: 14px; text-align: center; font-weight: 400; font-size: 11px; }
</style>
</head>
<body>
  <main class="spread">
    <section class="page page--left">
      <svg class="contents-art" width="420" height="594" viewBox="0 0 420 594">
        <defs>
          <linearGradient id="photoTone" x1="0" y1="0" x2="1" y2="1">
            <stop offset="0" stop-color="#3f3f44"/>
            <stop offset="0.45" stop-color="#8d7a70"/>
            <stop offset="1" stop-color="#c9c7c6"/>
          </linearGradient>
          <path id="bandLine" d="M0 86 Q245 95 400 275"/>
        </defs>
        <path role="img" aria-label="Foto: Händedruck zweier Geschäftsleute im Anzug"
              d="M0 0 H420 V210 Q250 180 190 300 Q160 380 150 470 L0 520 Z"
              fill="url(#photoTone)"/>
        <path d="M0 60 Q260 70 400 250 L400 300 Q230 120 0 112 Z" fill="#d42a2e"/>
        <text class="contents-title" dy="7">
          <textPath href="#bandLine" startOffset="97%" text-anchor="end">INHALT</textPath>
        </text>
      </svg>
      <ol class="toc">
        <li class="toc__item"><span class="toc__page">39</span><div><div class="toc__label">Kommentar</div><div class="toc__sub">Lorem Ipsum</div></div></li>
        <li class="toc__item"><span class="toc__page">41</span><div><div class="toc__label">Maßnahmen-<br>Steuerungsvorschlag</div><div class="toc__sub">Lorem Ipsum</div></div></li>
        <li class="toc__item"><span class="toc__page">47</span><div><div class="toc__label">Dolor sit Amet</div><div class="toc__sub">Lorem Ipsum</div></div></li>
        <li class="toc__item"><span class="toc__page">55</span><div><div class="toc__label">Dolor sit Amet</div><div class="toc__sub">Lorem Ipsum</div></div></li>
        <li class="toc__item"><span class="toc__page">70</span><div><div class="toc__label">Dolor sit Amet</div><div class="toc__sub">Lorem Ipsum</div></div></li>
      </ol>
    </section>

    <section class="page page--right">
      <div class="report-card">
        <h1 class="report-card__title">Controlling 01-06/19<br>28.09.19</h1>
        <div class="report-card__row"><span>Produktplan<br>Verantwortlich</span><span class="report-card__value">07 Inneres<br>Senator Hollmann</span></div>
        <div class="report-card__row"><span>Einhaltung<br>Finanzdaten</span><span class="report-card__value">Land <span class="mark">✕</span><br>Stadt <span class="mark">✕</span></span></div>
        <div class="report-card__row"><span>Einhaltung<br>Personaldaten</span><span class="report-card__value">Land <span class="mark">✕</span><br>Stadt <span class="mark">✓</span></span></div>
        <div class="report-card__row"><span>Einhaltung<br>strategische Ziele</span><span class="report-card__value">Land <span class="mark">✓</span><br>Stadt <span class="mark">✓</span></span></div>
      </div>
    </section>
  </main>
</body>
</html>
```